Bluestone Advisory & Mgmt - Professional Business Cards

Hi!

I am a Real Estate Developer and Construction Consultant.

I have a lot of inspiration from previous designs and would be open to using the attached Designs as a starting point. I would like to see these styles incorporated into your designs.

I really need professional business card to go with it that includes my important info.

Look forward to seeing your designs!.

Target Market(s)

My Target market are building owners, lawyers, consultants.

Industry/Entity Type

Real Estate Development

Contact Information for Business Card

My Name: Dorian Pelkey
My Title: Principle
Company Name: Bluestone Advisory & Mgmt, LLC
Address: 348 West 71st Street, 9th FL New York, NY 10010
Mobile: 917.806.3971
Website: bam-hvx.example

Font styles to use
Serif
Sans Serif

Colors

Designer to choose colors to be used in the design.

Requirements
Must have
• Must incorporate the logo attached or have new that looks similar.
• Must use professional font that will be seen and judged by wealthy land owners and developers.
• Must incorporate some of the color green.
Should not have
• Photo's or pictures of people or buildings of any kind.

```html
<!DOCTYPE html>
<html lang="en">
<head>
<meta charset="utf-8">
<title>Bluestone Advisory &amp; Mgmt - Business Card</title>
<link rel="stylesheet" href="https://fonts.googleapis.com/css2?family=Arimo:wght@400;700&display=swap">
<style>
  :root {
    --backdrop: #e6e6e4;
    --card-dark: #0b0904;
    --card-olive: #3d2d05;
    --text-light: #d3ccb4;
    --text-muted: #a59c7c;
    --text-faint: #8a8064;
    --accent-green: #7fa04a;
    --accent-green-deep: #2c3a12;
    --back-grey: #7a7a7a;
    --back-ink: #2e2e2e;
  }
  html, body {
    margin: 0;
    width: 1200px;
    height: 1200px;
    overflow: hidden;
    background: var(--backdrop);
    font-family: "Arimo", Arial, sans-serif;
  }
  .card {
    position: absolute;
    left: 255px;
    width: 693px;
    height: 396px;
  }
  .card-front { top: 181px; box-shadow: 0 0 0 1px #000; }
  .card-back {
    top: 630px;
    background: var(--back-grey);
    display: flex;
    align-items: center;
    justify-content: center;
  }
  .card-back::after {
    content: "";
    position: absolute;
    left: 0;
    right: 0;
    bottom: 0;
    height: 6px;
    background: var(--accent-green);
  }
  .card svg { display: block; }
  .brand-name {
    font-family: "Arimo", Arial, sans-serif;
    font-weight: 700;
    font-size: 78px;
    letter-spacing: 1px;
    color: var(--back-ink);
  }
</style>
</head>
<body>

<section class="card card-front">
  <svg width="693" height="396" viewBox="0 0 693 396">
    <defs>
      <linearGradient id="front-bg" x1="0" y1="0" x2="1" y2="1">
        <stop offset="0" stop-color="var(--card-dark)"/>
        <stop offset="1" stop-color="var(--card-olive)"/>
      </linearGradient>
      <linearGradient id="name-band" x1="0" y1="0" x2="0" y2="1">
        <stop offset="0" stop-color="#1a1406" stop-opacity="0.6"/>
        <stop offset="1" stop-color="#3b2c06"/>
      </linearGradient>
      <linearGradient id="disc-fill" x1="0" y1="0" x2="1" y2="1">
        <stop offset="0" stop-color="#1e1707"/>
        <stop offset="1" stop-color="var(--accent-green-deep)"/>
      </linearGradient>
      <clipPath id="card-clip"><rect width="693" height="396"/></clipPath>
    </defs>
    <rect class="card-bg" width="693" height="396" fill="url(#front-bg)"/>
    <rect class="name-band" x="0" y="135" width="451" height="95" fill="url(#name-band)"/>
    <line class="name-band-edge" x1="0" y1="230" x2="451" y2="230" stroke="var(--accent-green)" stroke-width="1" opacity="0.6"/>
    <g clip-path="url(#card-clip)">
      <circle class="corner-disc" role="img" aria-label="Hatched decorative disc" cx="700" cy="254" r="245" fill="url(#disc-fill)" opacity="0.7"/>
    </g>

    <text class="person-name" x="248" y="192" text-anchor="middle" font-family="Arimo, sans-serif" font-size="43" fill="var(--text-light)">Dorian Pelkey</text>
    <g class="person-title">
      <line x1="164" y1="209" x2="188" y2="209" stroke="var(--accent-green)" stroke-width="1.4"/>
      <text x="248" y="217" text-anchor="middle" font-family="Arimo, sans-serif" font-size="25" fill="var(--text-muted)">Principle</text>
      <line x1="308" y1="209" x2="332" y2="209" stroke="var(--accent-green)" stroke-width="1.4"/>
    </g>

    <g class="contact-phone">
      <circle cx="65" cy="320" r="16" fill="none" stroke="var(--accent-green)" stroke-width="2"/>
      <path d="M57 329 q-2 -4 2 -9 l6 -7 q3 -3 5 -1 l2 2 -4 4 -2 -1 -5 6 1 2 -3 4 z" fill="var(--text-light)"/>
      <text x="91" y="330" font-family="Arimo, sans-serif" font-size="23" fill="var(--text-light)">917.806.3971</text>
    </g>
    <g class="contact-web" fill="none" stroke="var(--accent-green)" stroke-width="1.3">
      <circle cx="282" cy="320" r="16"/>
      <ellipse cx="282" cy="320" rx="7" ry="16"/>
      <line x1="266" y1="320" x2="298" y2="320"/>
      <line x1="268" y1="312" x2="296" y2="312"/>
      <line x1="268" y1="328" x2="296" y2="328"/>
      <line x1="282" y1="304" x2="282" y2="336"/>
    </g>
    <text class="contact-web-text" x="308" y="327" font-family="Arimo, sans-serif" font-size="22" fill="var(--text-muted)">bam-hvx.example</text>

    <g class="company-block" font-family="Arimo, sans-serif">
      <text transform="translate(574 199) rotate(-90)" text-anchor="middle" font-size="23" fill="var(--text-faint)">Bluestone Advisory</text>
      <text transform="translate(602 199) rotate(-90)" text-anchor="middle" font-size="23" fill="var(--text-faint)">&amp; Mgmt, LLC</text>
      <line x1="613" y1="30" x2="613" y2="366" stroke="var(--accent-green)" stroke-width="1.4"/>
      <text transform="translate(631 199) rotate(-90)" text-anchor="middle" font-size="13.5" fill="var(--text-faint)">348 West 71st Street,</text>
      <text transform="translate(650 199) rotate(-90)" text-anchor="middle" font-size="13.5" fill="var(--text-faint)">9th FL New York, NY 10010</text>
    </g>
  </svg>
</section>

<section class="card card-back">
  <span class="brand-name">Bluestone</span>
</section>

</body>
</html>
```